Corvellan Hotel

A Hotel (Pub) in Sydney CBD. Posters will be outside of Hotel informing People what is on in Hotel.
We will be Printing in A1 size.
CORVELLAN HOTEL
Open 9am - 3am 7 Days
Monday - Thursday
Happy Hour
4pm - 6pm
Local Beer & Wine
Wednesday
Poker Night: Great $$$ Prizes
Everyday
Steak or Schniztels: Served with Mashed Potato & Salad or Chips & Salad - $8.50
Live Sport on the Big Screen
BISTRO
OPEN 7 DAYS 12- 9pm
Daily Blackboard Specials + Full Menu Inside
Best service in Town
Male or Female 18 to Seniors.Passing Trade.
Hotel

```html
<!DOCTYPE html>
<html lang="en">
<head>
<meta charset="utf-8">
<title>Corvellan Hotel – What's On</title>
<link rel="stylesheet" href="https://fonts.googleapis.com/css2?family=Montserrat:ital,wght@0,700;0,800;1,700;1,800&family=Roboto+Condensed:wght@400;700&family=Roboto:wght@400;500&display=swap">
<style>
  :root {
    --page: #ffffff;
    --maroon-light: #6a4448;
    --maroon-dark: #2c1618;
    --white: #ffffff;
    --ink: #111111;
    --shadow: #000000;
    --amber-top: #fff3d6;
    --amber: #f29a12;
    --green-top: #c8f0d0;
    --green: #1d8a3c;
    --red-top: #ffb0b0;
    --red: #d81414;
    --blue-top: #ffffff;
    --blue: #8fb0e6;
    --beer: #f39a1a;
    --chip: #1f9a45;
    --steak: #a83238;
    --ball: #e8e8e8;
  }
  * { margin: 0; padding: 0; box-sizing: border-box; }
  html, body { width: 1200px; height: 900px; overflow: hidden; background: var(--page); }
  .canvas { position: relative; width: 1200px; height: 900px; }
  .poster {
    position: absolute; left: 283px; top: 0; width: 636px; height: 900px;
    background: radial-gradient(ellipse at 50% 55%, var(--maroon-light) 0%, #4a2a2d 55%, var(--maroon-dark) 100%);
  }
  .frame { position: absolute; left: 0; top: 0; width: 1200px; height: 900px; pointer-events: none; }
  .abs { position: absolute; }
  .title {
    left: 283px; width: 636px; top: 14px; text-align: center;
    font-family: "Montserrat", sans-serif; font-weight: 800; color: var(--white);
    font-size: 56px; line-height: 54px; letter-spacing: 1px;
    text-shadow: 4px 4px 0 var(--shadow);
  }
  .title-mark { left: 590px; top: 140px; width: 20px; height: 20px; background: var(--white); border-radius: 2px; transform: rotate(45deg); }
  .hours {
    left: 283px; width: 636px; top: 178px; text-align: center;
    font-family: "Montserrat", sans-serif; font-style: italic; font-weight: 700;
    color: var(--white); font-size: 37px; text-shadow: 3px 3px 0 var(--shadow);
  }
  .hours .days { margin-left: 44px; }
  .art { position: absolute; }
  .art-beer { left: 328px; top: 266px; width: 109px; height: 196px; border-radius: 50px 50px 26px 26px / 20px 20px 20px 20px; background: linear-gradient(90deg, #f6b84a, var(--beer) 50%, #d8780a); border: 3px solid var(--ink); }
  .art-chips { left: 620px; top: 343px; width: 102px; height: 135px; border-radius: 50px / 22px; background: linear-gradient(180deg, #35b45c, var(--chip)); border: 3px solid var(--ink); }
  .art-ball { left: 808px; top: 495px; width: 66px; height: 66px; border-radius: 50%; background: radial-gradient(circle at 40% 35%, #ffffff, var(--ball)); border: 2px solid var(--ink); }
  .art-steak { left: 340px; top: 588px; width: 214px; height: 115px; border-radius: 60% 45% 40% 55%; background: radial-gradient(ellipse at 50% 40%, #c24048, var(--steak) 60%, #d99a9e 85%); border: 3px solid var(--ink); }
  .heading {
    font-family: "Roboto Condensed", sans-serif; font-weight: 700; line-height: 1; white-space: nowrap;
    -webkit-background-clip: text; background-clip: text; color: transparent;
    filter: drop-shadow(3px 3px 0 var(--shadow));
  }
  .happy-hour { left: 445px; width: 152px; top: 268px; font-size: 50px; line-height: 48px; text-align: right; letter-spacing: 1px;
    background-image: linear-gradient(180deg, var(--amber-top), var(--amber) 70%); }
  .poker-night { left: 619px; top: 284px; font-size: 48px; letter-spacing: -0.3px;
    background-image: linear-gradient(180deg, var(--green-top), var(--green) 70%); }
  .live-sport { left: 328px; top: 515px; font-size: 36px; letter-spacing: -0.2px; z-index: 2;
    background-image: linear-gradient(180deg, var(--red-top), var(--red) 60%); }
  .bistro { left: 653px; top: 574px; font-size: 50px; letter-spacing: 1px;
    background-image: linear-gradient(180deg, var(--blue-top), var(--blue) 80%); }
  .strong { font-family: "Roboto Condensed", sans-serif; font-weight: 700; color: var(--white); text-shadow: 2px 2px 0 var(--shadow); line-height: 1.15; white-space: nowrap; }
  .plain { font-family: "Roboto", sans-serif; font-weight: 400; color: var(--white); line-height: 1.25; white-space: nowrap; }
  .happy-days { left: 400px; width: 198px; top: 378px; text-align: right; font-size: 35px; letter-spacing: .5px; }
  .happy-note { left: 338px; top: 469px; font-size: 25px; letter-spacing: .9px; }
  .poker-day { left: 732px; top: 351px; font-size: 32px; letter-spacing: -0.3px; }
  .poker-prize { left: 733px; width: 140px; top: 399px; text-align: center; font-size: 26px; line-height: 32px; letter-spacing: .8px; }
  .bistro-hours { left: 588px; top: 630px; font-size: 34px; }
  .bistro-menu { left: 582px; top: 676px; font-size: 25px; line-height: 34px; letter-spacing: .3px; }
  .steak-title { left: 328px; top: 715px; font-size: 31px; }
  .steak-days { left: 328px; top: 752px; font-size: 34px; letter-spacing: 2px; }
  .steak-note { left: 330px; top: 797px; font-family: "Roboto Condensed", sans-serif; font-size: 25px; line-height: 28px; color: var(--white); white-space: nowrap; }
  .best-service { right: 332px; top: 760px; text-align: right; font-family: "Montserrat", sans-serif; font-style: italic; font-weight: 800; font-size: 24px; line-height: 32px; color: var(--ink); }
</style>
</head>
<body>
<main class="canvas">
  <section class="poster"></section>

  <svg class="frame" viewBox="0 0 1200 900" aria-hidden="true">
    <path d="M368 48 H337 A32 32 0 0 0 305 80 V845 A32 32 0 0 0 337 877 H865 A32 32 0 0 0 897 845 V80 A32 32 0 0 0 865 48 H834"
          fill="none" stroke="var(--white)" stroke-width="6"/>
    <polygon class="starburst" fill="var(--white)"
      points="715,877 751,866 719,846 756,840 729,813 767,815 747,783 783,793 770,757 804,775 798,737 827,761 829,723 853,753 863,716 878,750 878,877"/>
  </svg>

  <h1 class="abs title">CORVELLAN<br>HOTEL</h1>
  <div class="abs title-mark" role="img" aria-label="Small diamond ornament"></div>
  <p class="abs hours">OPEN 9AM - 3AM<span class="days">7 DAYS</span></p>

  <div class="art art-beer" role="img" aria-label="Illustration of a pint of beer"></div>
  <h2 class="abs heading happy-hour">HAPPY<br>HOUR</h2>
  <p class="abs strong happy-days">Mon-Thurs<br>4 - 6pm</p>
  <p class="abs plain happy-note">Local beer and wine</p>

  <h2 class="abs heading poker-night">POKER NIGHT</h2>
  <div class="art art-chips" role="img" aria-label="Illustration of a stack of green poker chips"></div>
  <p class="abs strong poker-day">Wednesday</p>
  <p class="abs plain poker-prize">Great $$$<br>Prizes</p>

  <div class="art art-ball" role="img" aria-label="Illustration of a soccer ball"></div>
  <h2 class="abs heading live-sport">LIVE SPORT ON THE BIG SCREEN</h2>

  <div class="art art-steak" role="img" aria-label="Illustration of a raw steak"></div>
  <h2 class="abs heading bistro">BISTRO</h2>
  <p class="abs strong bistro-hours">Open 7 days 12-9pm</p>
  <p class="abs plain bistro-menu">Daily Blackboard Specials<br>+ Full Menu Inside</p>

  <p class="abs strong steak-title">Steak or Schniztels</p>
  <p class="abs strong steak-days">Everyday</p>
  <p class="abs steak-note">Served with Mashed Potato &amp; Salad<br>or Chips &amp; Salad - $8.50</p>

  <p class="abs best-service">Best<br>service<br>in Town!</p>
</main>
</body>
</html>
```